Landscape Company Stationary
Biz cards, letterhead, envelopes, etc
Professional
Dean Morvik
P.O. Box 3852
Sparta, NJ 07634
foxridgemail@postbrim.com
Dont want address on biz cards, just letterhead and envelopes. Would like to incorporate the stripe and colors that are in our logo.
Logo with colors and fonts to use. Please incorporate the striping too and colors

```html
<!DOCTYPE html>
<html lang="en">
<head>
<meta charset="utf-8">
<title>Foxridge Landscapes – Business Card</title>
<link rel="stylesheet" href="https://fonts.googleapis.com/css2?family=Open+Sans:wght@400;700;800&display=swap">
<style>
  :root {
    --backdrop: #4a4a48;
    --card: #ffffff;
    --card-shade: #eeeeee;
    --green-dark: #1e7a2c;
    --green-light: #8dc63f;
    --leaf-faint: #e3eadf;
    --ink: #3a3a3a;
    --muted: #777777;
  }
  * { margin: 0; padding: 0; box-sizing: border-box; }
  html, body { width: 1200px; height: 749px; overflow: hidden; }
  body {
    background: var(--backdrop);
    font-family: "Open Sans", Arial, sans-serif;
    position: relative;
  }
  .card {
    position: absolute;
    width: 460px;
    height: 263px;
    border-radius: 14px;
    background: linear-gradient(180deg, var(--card) 0%, var(--card) 50%, var(--card-shade) 100%);
    overflow: hidden;
  }
  .card-front { left: 110px; top: 170px; }
  .card-back  { left: 630px; top: 316px; }

  .brand {
    position: absolute;
    display: flex;
    align-items: center;
    gap: 8px;
    white-space: nowrap;
  }
  .brand-mark {
    width: 16px; height: 16px;
    border-radius: 50%;
    background: var(--green-light);
    flex: none;
  }
  .brand-name {
    color: var(--green-dark);
    font-weight: 800;
    font-size: 22px;
    line-height: 1;
    letter-spacing: -.3px;
  }
  .card-front .brand { left: 150px; top: 46px; }
  .card-back .brand  { left: 0; right: 0; top: 112px; justify-content: center; }

  .leaf-art {
    position: absolute;
    left: 250px;
    top: 120px;
    width: 70px;
    height: 80px;
    border-radius: 50% 50% 50% 50% / 60% 60% 40% 40%;
    background: radial-gradient(circle at 50% 45%, var(--leaf-faint), rgba(227,234,223,0) 72%);
  }

  .contact {
    position: absolute;
    left: 22px;
    top: 136px;
    color: var(--ink);
    font-size: 10px;
    line-height: 14px;
  }
  .contact-name { color: var(--green-dark); font-weight: 700; font-size: 12.5px; line-height: 16px; }
  .contact-role { color: var(--muted); font-size: 10px; line-height: 12px; margin-bottom: 6px; }
  .contact dt { display: inline; font-weight: 700; }
  .contact dd { display: inline; margin-left: 2px; }
  .contact dd::after { content: ""; display: block; }

  .stripe {
    position: absolute;
    left: 0; right: 0; bottom: 0;
    height: 30px;
  }
  .stripe svg { display: block; }
</style>
</head>
<body>
  <section class="card card-front" aria-label="Business card front">
    <div class="brand">
      <span class="brand-mark"></span>
      <span class="brand-name">Foxridge Landscapes</span>
    </div>
    <div class="leaf-art" role="img" aria-label="Faint leaf decoration"></div>
    <div class="contact">
      <p class="contact-name">Dean Morvik</p>
      <p class="contact-role">Owner</p>
      <dl>
        <dt>Phone:</dt><dd>973-555-0148</dd>
        <dt>Cell:</dt><dd>862-555-0193</dd>
        <dt>Email:</dt><dd>foxridgemail@postbrim.com</dd>
      </dl>
    </div>
    <div class="stripe">
      <svg width="460" height="30" viewBox="0 0 460 30" aria-hidden="true">
        <rect x="0" y="6" width="460" height="5" fill="var(--green-light)"/>
        <rect x="0" y="13" width="460" height="17" fill="var(--green-dark)"/>
      </svg>
    </div>
  </section>

  <section class="card card-back" aria-label="Business card back">
    <div class="brand">
      <span class="brand-mark"></span>
      <span class="brand-name">Foxridge Landscapes</span>
    </div>
  </section>
</body>
</html>
```